KT Prime Motion personal training needs a new Business Card design for 2016

Business Card design:
Our current business card is very plain
We are bringing on our first team member next year and thought its a perfect time to have a new face lift for our company!

We are a Personal Training business "KT Prime Motion" who specializes in strength and conditioning / weightloss training,
We also run a yearly Bootcamp called "Ferocity Drillcamps", this is our Logo Design which we are looking for

The pink and blue in the logo are our business colours, how ever we don't want those colours to heavily dominate the card.

We are looking for a business card which is eye catching, and creative.

I am open to suggestions and any designs :)

Logo Design:

For our Logo Design we are looking for a bright, energetic logo, preferably a word logo which portrays strength and high intensity
If it has icon's etc in it thats fine again im open for suggestions :)
The Logo Design is for our Bootcamp which runs yearly
The bootcamp is called "Ferocity Drillcamp"

Target Market(s)

Age 20-40
Individuals who want to look great and have more energy

Industry/Entity Type

Business

Contact Information for Business Card

On the front
KT Prime Motion Doriel Maxton Personal Training / Bootcamps / Pilates / Nutrition Healthy mind, Healthy body, Ultimate lifestyle < our slogan
Icons for the following
Email:
Mobile:
Facebook:
Instagram:

On the back we would like to include somewhere
"Show this card to receive 50% off your first 30min pt session"
"Valid to one user only"

Logo Text

Ferocity Drillcamp

Font styles to use
Serif

Colors
e34197
0255a3
000000
ffffff

Requirements
Must have
• - Icons for instagram, facebook, email and mobile phone
• - Slogan: Healthy mind, Healthy body, Ultimate lifestyle
• - What we offer: Personal Training , Bootcamps, Pilates, Nutrition
• - Logo
• -
Nice to have
• - Our 50% offer on the back
• - a place for a photo
Should not have
• - Pink and Blue everywhere

```html
<!DOCTYPE html>
<html lang="en">
<head>
<meta charset="utf-8">
<title>KT Prime Motion – Business Card</title>
<link rel="stylesheet" href="https://fonts.googleapis.com/css2?family=Great+Vibes&family=Marck+Script&family=Montserrat:wght@800&family=Open+Sans:wght@400&display=swap">
<style>
  :root {
    --brand-blue: #1a5fad;
    --brand-pink: #e066a3;
    --line-pink: #e065a8;
    --ink-dark: #222;
    --paper: #ffffff;
    --ghost-grey: #e3e6e9;
    --shadow: rgba(0,0,0,0.35);
  }
  html, body {
    margin: 0;
    padding: 0;
    width: 1200px;
    height: 1174px;
    overflow: hidden;
    background: var(--paper);
  }
  .canvas {
    position: relative;
    width: 1200px;
    height: 1174px;
  }
  .card {
    position: absolute;
    left: 273px;
    width: 660px;
    border: 1.5px solid var(--ink-dark);
    box-shadow: 10px 12px 8px -2px var(--shadow);
    overflow: hidden;
    background: var(--paper);
  }
  .card--front { top: 135px; height: 376px; }
  .card--back  { top: 631px; height: 375px; }

  /* front */
  .front-ghost-mark {
    position: absolute;
    left: 506px;
    top: -8px;
    width: 136px;
    height: 136px;
    border-radius: 50%;
    background: var(--ghost-grey);
  }
  .brand-lockup {
    position: absolute;
    left: 45px;
    top: 30px;
    display: flex;
    flex-direction: column;
    align-items: center;
    gap: 10px;
  }
  .brand-dot {
    width: 66px;
    height: 66px;
    border-radius: 50%;
    background: var(--brand-blue);
  }
  .brand-name {
    font-family: "Montserrat", sans-serif;
    font-weight: 800;
    font-size: 27px;
    color: var(--brand-blue);
    letter-spacing: 0.5px;
    white-space: nowrap;
  }
  .tagline-script {
    position: absolute;
    right: 24px;
    top: 196px;
    font-family: "Great Vibes", cursive;
    font-size: 25px;
    color: var(--brand-blue);
    white-space: nowrap;
  }
  .front-rule {
    position: absolute;
    left: 0;
    top: 245px;
    width: 472px;
    height: 2px;
    background: var(--line-pink);
  }
  .services {
    position: absolute;
    right: 24px;
    top: 234px;
    font-family: "Open Sans", sans-serif;
    font-size: 15px;
    color: var(--brand-pink);
  }
  .front-band {
    position: absolute;
    left: 0;
    top: 262px;
    width: 100%;
    height: 114px;
    background: var(--brand-blue);
  }
  .contact-list {
    position: absolute;
    left: 46px;
    top: 37px;
    margin: 0;
    padding: 0;
    list-style: none;
    font-family: "Open Sans", sans-serif;
    font-size: 12.5px;
    line-height: 17.5px;
    color: var(--brand-pink);
  }

  /* back */
  .offer-panel {
    position: absolute;
    left: 0;
    top: 0;
    width: 100%;
    height: 295px;
    background: var(--brand-pink);
  }
  .offer-text {
    position: absolute;
    left: 0;
    top: 0;
    width: 660px;
    height: 295px;
  }
  .offer-text text {
    font-family: "Marck Script", cursive;
    fill: var(--paper);
  }
  .back-band {
    position: absolute;
    left: 0;
    top: 295px;
    width: 100%;
    height: 80px;
    background: var(--brand-blue);
  }
  .validity {
    position: absolute;
    left: 0;
    top: 14px;
    width: 100%;
    text-align: center;
    font-family: "Open Sans", sans-serif;
    font-size: 21px;
    color: var(--brand-pink);
  }
  .validity-rule {
    position: absolute;
    top: 25px;
    height: 2px;
    background: var(--line-pink);
  }
  .validity-rule--left  { left: 0; width: 182px; }
  .validity-rule--right { left: 477px; width: 183px; }
</style>
</head>
<body>
<main class="canvas">

  <section class="card card--front" aria-label="Business card front">
    <div class="front-ghost-mark" aria-hidden="true"></div>

    <div class="brand-lockup">
      <div class="brand-dot" aria-hidden="true"></div>
      <div class="brand-name">KT PRIME MOTION</div>
    </div>

    <p class="tagline-script" style="margin:0">KT Prime Motion Doriel Maxton Personal Training</p>
    <div class="front-rule"></div>
    <p class="services" style="margin:0">Bootcamps / Pilates</p>

    <div class="front-band">
      <ul class="contact-list">
        <li>tel.: +00 (000) 000-00-00</li>
        <li>fax: +00 (000) 000-00-00</li>
        <li>E-mail: kt@primemotion.com</li>
      </ul>
    </div>
  </section>

  <section class="card card--back" aria-label="Business card back">
    <div class="offer-panel">
      <svg class="offer-text" viewBox="0 0 660 295" aria-label="Show this card to receive 50% off your first 30min pt session">
        <text x="321" y="150" font-size="46" text-anchor="middle" transform="rotate(-12.5 321 150)">Show this card to receive 50%</text>
        <text x="312" y="194" font-size="29" text-anchor="middle" transform="rotate(-12.5 312 194)">off your first 30min pt session</text>
      </svg>
    </div>
    <div class="back-band">
      <span class="validity-rule validity-rule--left"></span>
      <p class="validity" style="margin:0">Valid to one user only</p>
      <span class="validity-rule validity-rule--right"></span>
    </div>
  </section>

</main>
</body>
</html>
```